Norvale Email Signature Banners – Fabrication Capability Series

www.Norvale.com.au is an Australian engineering and fabrication company specialising in fabrication and welding of :
steel piping spools,
skids and frames,
small volume process steel tanks
and general steel fabrication
We require four distinct banner designs for use in Teldrin Quillmark email signatures. Each banner will highlight a specific capability while maintaining a consistent brand identity.
Deliverables
Four banners total:
Piping Spools Fabrication – focus on precision welding and stainless steel pipework
Skid & Frames Fabrication – highlight skid systems and structural frames
Small Steel Tanks Fabrication – show fabricated tanks and workshop craftsmanship
General Fabrication Solutions – broad steel fabrication theme for company-wide use
Dimensions: 600–700 px wide × 100 px high
Format: PNG (preferred), small file size prefered
Resolution: 72 dpi
Background: non-transparent, industrial or workshop setting
Text examples:
1. Piping Spools Fabrication
Option A: “Expert Fabrication Solutions for Process Piping”
Option B: “Precision Welding for Complex Systems”
Option C: “Delivering Quality in Every Spool”
Option D: “Engineered for Flow, Built for Strength”
2. Skid & Frames Fabrication
Option A: “Custom Engineered Modular Systems”
Option B: “Built Strong. Designed Smart.”
Option C: “Reliable Frames for Industrial Performance”
Option D: “Modular Fabrication for Seamless Integration”
3. Small Steel Tanks Fabrication
Option A: “Precision Built for Your Needs”
Option B: “Compact Strength. Proven Durability.”
Option C: “Fabricated for Performance and Longevity”
Option D: “Small Tanks. Big Reliability.”
4. General Fabrication Solutions
Option A: “Quality Craftsmanship, Proven Results”
Option B: “Your Partner in Precision Fabrication”
Option C: “Engineering Excellence in Every Weld”
Option D: “Australian Fabrication. Global Standards.”
Style Direction
Clean, professional, and engineering‑focused
Use Norvale brand colours
Blend photo realism with vector clarity (no heavy gradients)
Include subtle industrial textures or workshop imagery
Typography: bold sans‑serif, legible at small scale
Usage Context
These banners will appear at the bottom of staff email signatures via Quillmark Email Signature Tool for Teldrin 365, so clarity and fast loading are essential. No Logo is required in the banners.
Reference
Existing Norvale signature is attached. Colour palette to match the signature style and logo.
Target Market(s)
Engineering and construction companies,
Industry/Entity Type
Engineering fabrication design

```html
<!DOCTYPE html>
<html lang="en">
<head>
<meta charset="utf-8">
<title>Piping Spools Fabrication – Option B</title>
<link rel="stylesheet" href="https://fonts.googleapis.com/css2?family=Figtree:wght@700;800&display=swap">
<style>
  :root {
    --page-bg: #ffffff;
    --ink: #0a0a0a;
    --brand-blue: #1da9e1;
    --steel-grey: #97989d;
    --band-text: #ffffff;
    --photo-dark: #2f3337;
    --photo-mid: #6d6358;
    --photo-light: #b9bcbf;
  }
  * { margin: 0; padding: 0; box-sizing: border-box; }
  html, body {
    width: 1200px;
    height: 1000px;
    overflow: hidden;
    background: var(--page-bg);
  }
  .sheet {
    position: relative;
    width: 1200px;
    height: 1000px;
    font-family: "Figtree", Arial, sans-serif;
  }
  .sheet-title {
    position: absolute;
    left: 77px;
    top: 42px;
    font-weight: 800;
    font-size: 25px;
    line-height: 31px;
    color: var(--ink);
    letter-spacing: -0.2px;
  }
  .banner {
    position: absolute;
    left: 250px;
    width: 700px;
    height: 100px;
    overflow: hidden;
  }
  .banner--one { top: 178px; }
  .banner--two { top: 364px; }
  .banner--three { top: 556px; }
  .banner--four { top: 743px; }

  .workshop-photo {
    background:
      linear-gradient(90deg,
        var(--photo-dark) 0%,
        #4b4f52 18%,
        var(--photo-mid) 34%,
        #8c8f93 50%,
        var(--photo-light) 66%,
        #8d9296 82%,
        var(--photo-dark) 100%);
  }

  /* stacked layout: photo strip over caption band */
  .banner--stacked .workshop-photo {
    position: absolute;
    left: 0; top: 0;
    width: 100%;
    height: 60px;
  }
  .banner--stacked .caption-band {
    position: absolute;
    left: 0; top: 60px;
    width: 100%;
    height: 40px;
    display: flex;
    align-items: center;
    justify-content: center;
  }
  .banner--stacked .tagline {
    font-weight: 800;
    font-size: 25px;
    color: var(--band-text);
    letter-spacing: 0.1px;
  }

  /* split layout: text panel beside photo */
  .banner--split .caption-band {
    position: absolute;
    left: 0; top: 0;
    width: 370px;
    height: 100%;
    display: flex;
    align-items: center;
    padding-left: 27px;
  }
  .banner--split .workshop-photo {
    position: absolute;
    left: 370px; top: 0;
    width: 330px;
    height: 100%;
  }
  .banner--split .tagline {
    font-weight: 800;
    font-size: 27px;
    line-height: 32px;
    color: var(--band-text);
  }

  .band--blue { background: var(--brand-blue); }
  .band--grey { background: var(--steel-grey); }

  .page-number {
    position: absolute;
    left: 1156px;
    top: 970px;
    font-family: Arial, Helvetica, sans-serif;
    font-size: 10px;
    color: var(--ink);
  }
</style>
</head>
<body>
<main class="sheet">
  <h1 class="sheet-title">1. Piping Spools Fabrication<br>Option B: “Precision Welding for Complex Systems”</h1>

  <section class="banner banner--stacked banner--one">
    <div class="workshop-photo" role="img" aria-label="Welder in a leather jacket and gloves welding stainless steel pipe spools in a workshop"></div>
    <div class="caption-band band--blue"><p class="tagline">Precision Welding for Complex Systems</p></div>
  </section>

  <section class="banner banner--split banner--two">
    <div class="caption-band band--blue"><p class="tagline">Precision Welding for<br>Complex Systems</p></div>
    <div class="workshop-photo" role="img" aria-label="Welder working on a stainless steel pipe spool assembly with flanges in a fabrication workshop"></div>
  </section>

  <section class="banner banner--stacked banner--three">
    <div class="workshop-photo" role="img" aria-label="Welder in a leather jacket and gloves welding stainless steel pipe spools in a workshop"></div>
    <div class="caption-band band--grey"><p class="tagline">Precision Welding for Complex Systems</p></div>
  </section>

  <section class="banner banner--split banner--four">
    <div class="caption-band band--grey"><p class="tagline">Precision Welding for<br>Complex Systems</p></div>
    <div class="workshop-photo" role="img" aria-label="Welder working on a stainless steel pipe spool assembly with flanges in a fabrication workshop"></div>
  </section>

  <p class="page-number">004</p>
</main>
</body>
</html>
```